HomeBridle business card and stationary design

We are looking for a simple yet elegant design for our mortgage company business card and stationary.

The card should include:
Name (Derek Walsh)
Title (CEO)
Phone Number (614-208-3917)
Address (48 Birchfield Court, Suite 314, Marlow, OH 43952)
Email (email@homebridle-example.com)
"NMLS" i.e. (NMLS 61947)
"Company NMLS" (Company NMLS 472815)

See above

```html
<!DOCTYPE html>
<html lang="en">
<head>
<meta charset="utf-8">
<title>HomeBridle Stationery</title>
<link href="https://fonts.googleapis.com/css2?family=Montserrat:wght@400;500;600;700&family=Courgette&display=swap" rel="stylesheet">
<style>
  :root{
    --blue:#0aa0dc;
    --navy:#14213a;
    --paper:#f2f2f3;
    --ground:#e4e4e6;
    --ink:#1d1d22;
  }
  *{margin:0;padding:0;box-sizing:border-box}
  html,body{width:1200px;height:792px;overflow:hidden}
  body{background:var(--ground);font-family:"Montserrat",sans-serif;color:var(--ink);position:relative}
  .sheet{position:absolute;background:var(--paper);box-shadow:0 3px 10px rgba(0,0,0,.12);overflow:hidden}
  .band{position:absolute;left:0;width:100%;display:block}
  .brand{font-family:"Montserrat",sans-serif;font-weight:500;color:var(--navy);letter-spacing:-.01em;white-space:nowrap;display:flex;align-items:center}
  .brand-mark{display:inline-block;background:var(--blue);margin-right:.25em;width:.4em;height:.4em}
  .person-name{font-weight:700;color:var(--blue);white-space:nowrap}
  .person-name b{color:var(--navy)}
  .person-title{font-weight:600;color:var(--navy);white-space:nowrap}
  .contact-list{list-style:none}
  .contact-list li{display:flex;align-items:flex-start;font-weight:600;color:var(--navy)}
  .contact-list svg{flex:none}
  .web{color:var(--navy)}
  .web span{color:var(--blue)}

  /* business card front */
  .card-front{left:166px;top:72px;width:158px;height:90px}
  .card-front .brand{position:absolute;left:0;right:0;top:30px;justify-content:center;font-size:19px}
  .card-front .web{position:absolute;left:0;right:0;top:55px;text-align:center;font-size:4.6px;font-weight:600}

  /* business card back */
  .card-back{left:166px;top:182px;width:158px;height:90px}
  .card-back .brand{position:absolute;left:8px;top:37px;font-size:12px}
  .card-back .person{position:absolute;left:83px;top:8px}
  .card-back .person-name{font-size:6.5px}
  .card-back .person-title{font-size:4.3px;margin-top:1px}
  .card-back .contact-list{position:absolute;left:83px;top:32px;width:72px}
  .card-back .contact-list li{font-size:3.9px;line-height:4.6px;margin-bottom:3px}
  .card-back .contact-list svg{width:6px;height:6px;margin-right:4px}
  .card-back .nmls{position:absolute;right:8px;bottom:1px;font-size:4.2px;color:#fff;font-weight:500;line-height:6px}

  /* letterhead */
  .letterhead{left:372px;top:104px;width:295px;height:416px}
  .letterhead .brand{position:absolute;left:26px;top:32px;font-size:21px}
  .letterhead .person{position:absolute;left:183px;top:18px}
  .letterhead .person-name{font-size:9.5px}
  .letterhead .person-title{font-size:6.3px;margin-top:1px}
  .letter{position:absolute;left:26px;top:86px;width:242px}
  .salutation{font-size:7.5px;font-weight:500;margin-bottom:8px}
  .letter-body p{font-size:4.35px;line-height:5.65px;margin-bottom:5.6px;color:#333}
  .closing{position:absolute;left:26px;top:326px}
  .closing .sign-off{font-size:7.2px;font-weight:500}
  .signature{font-family:"Courgette",cursive;color:var(--blue);font-size:15px;margin-top:3px;line-height:20px}
  .closing .nmls{font-size:6.4px;font-weight:500;margin-top:4px;line-height:7.6px}
  .letter-footer{position:absolute;left:55px;top:388px;display:flex;gap:5px}
  .letter-footer li{font-size:3.5px;line-height:4.2px}
  .letter-footer svg{width:6px;height:6px;margin-right:3px}

  /* square envelope */
  .envelope{left:720px;top:72px;width:330px;height:164px}
  .envelope .brand{position:absolute;left:0;right:0;top:115px;justify-content:center;font-size:18px}

  /* folder */
  .folder{left:720px;top:253px;width:331px;height:439px}
  .folder .brand{position:absolute;left:0;right:0;top:205px;justify-content:center;font-size:34px;padding-left:18px}

  /* DL envelope */
  .dl-envelope{left:340px;top:564px;width:330px;height:164px}
  .dl-envelope .brand{position:absolute;left:22px;top:54px;font-size:17px}
  .dl-envelope .person{position:absolute;left:240px;top:16px}
  .dl-envelope .person-name{font-size:8.3px}
  .dl-envelope .person-title{font-size:5.3px;margin-top:1px}
  .dl-envelope .contact-list{position:absolute;left:20px;top:88px;width:140px}
  .dl-envelope .contact-list li{font-size:5.2px;line-height:6.3px;margin-bottom:4px;font-weight:500}
  .dl-envelope .contact-list svg{width:7px;height:7px;margin-right:5px}
  .dl-envelope .nmls{position:absolute;right:18px;bottom:2px;font-size:7px;color:#fff;line-height:11px}
</style>
</head>
<body>
<svg width="0" height="0" style="position:absolute" aria-hidden="true">
  <defs>
    <symbol id="icon-phone" viewBox="0 0 10 10"><circle cx="5" cy="5" r="5" fill="#0aa0dc"/><path d="M3.3 2.6l1 1-.5.6c.3.7.8 1.2 1.5 1.5l.6-.5 1 1-.6.9c-1.9-.3-3.5-1.9-3.8-3.8z" fill="#fff"/></symbol>
    <symbol id="icon-pin" viewBox="0 0 10 10"><path d="M5 .5a3.6 3.6 0 0 1 3.6 3.6C8.6 6.6 5 9.8 5 9.8S1.4 6.6 1.4 4.1A3.6 3.6 0 0 1 5 .5z" fill="#0aa0dc"/><circle cx="5" cy="4.1" r="1.4" fill="#fff"/></symbol>
    <symbol id="icon-mail" viewBox="0 0 10 10"><circle cx="5" cy="5" r="5" fill="#0aa0dc"/><rect x="2.6" y="3.3" width="4.8" height="3.4" fill="none" stroke="#fff" stroke-width=".7"/><path d="M2.6 3.3L5 5.3l2.4-2" fill="none" stroke="#fff" stroke-width=".7"/></symbol>
    <symbol id="icon-web" viewBox="0 0 10 10"><circle cx="5" cy="5" r="5" fill="#0aa0dc"/><circle cx="5" cy="5" r="2.7" fill="none" stroke="#fff" stroke-width=".6"/><ellipse cx="5" cy="5" rx="1.1" ry="2.7" fill="none" stroke="#fff" stroke-width=".6"/><path d="M2.3 5h5.4" stroke="#fff" stroke-width=".6"/></symbol>
  </defs>
</svg>

<!-- business card front -->
<section class="sheet card-front" aria-label="Business card front">
  <svg class="band" style="top:0;height:8px" viewBox="0 0 158 8" preserveAspectRatio="none"><rect width="158" height="7" fill="var(--blue)"/><path d="M0 0h29l-12 10H0z" fill="var(--navy)"/></svg>
  <div class="brand"><span class="brand-mark"></span>HomeBridle</div>
  <p class="web">www.<span>homebridle</span>.com</p>
  <svg class="band" style="bottom:0;height:12px" viewBox="0 0 158 12" preserveAspectRatio="none"><rect y="4" width="158" height="8" fill="var(--blue)"/><path d="M158 0h-21l-12 12h33z" fill="var(--navy)"/></svg>
</section>

<!-- business card back -->
<section class="sheet card-back" aria-label="Business card back">
  <div class="brand"><span class="brand-mark"></span>HomeBridle</div>
  <div class="person">
    <p class="person-name">Derek <b>Walsh</b></p>
    <p class="person-title">Business &amp; Personal Coach</p>
  </div>
  <ul class="contact-list">
    <li><svg><use href="#icon-phone"/></svg>614-208-3917</li>
    <li><svg><use href="#icon-pin"/></svg>48 Birchfield Court, Suite 314,<br>Marlow, OH 43952</li>
    <li><svg><use href="#icon-mail"/></svg>email@homebridle-example.com</li>
    <li><svg><use href="#icon-web"/></svg><span class="web">www.<span>homebridle</span>.com</span></li>
  </ul>
  <svg class="band" style="bottom:0;height:12px" viewBox="0 0 158 12" preserveAspectRatio="none"><rect y="4" width="158" height="8" fill="var(--blue)"/><path d="M0 0h16l12 12H0z" fill="var(--navy)"/><path d="M0 4h10l8 8H0z" fill="var(--paper)"/></svg>
  <p class="nmls">NMLS 61947 | NMLS 472815</p>
</section>

<!-- letterhead -->
<section class="sheet letterhead" aria-label="Letterhead">
  <div class="brand"><span class="brand-mark"></span>HomeBridle</div>
  <div class="person">
    <p class="person-name">Derek <b>Walsh</b></p>
    <p class="person-title">Business &amp; Personal Coach</p>
  </div>
  <div class="letter">
    <p class="salutation">Dear Sir,</p>
    <div class="letter-body">
      <p>Thank you for considering us for your home loan. Our team reviews every application with care, compares rates from many lenders, and explains each step in plain words. We help first-time buyers, families moving up, and owners who want to refinance. From the first call to the closing table, you will have one advisor who answers your questions and keeps the process moving on time.</p>
      <p>Please review the enclosed summary of options. If anything is unclear, call or write to us and we will gladly walk you through the details.</p>
      <p>Thank you for considering us for your home loan. Our team reviews every application with care, compares rates from many lenders, and explains each step in plain words. We help first-time buyers, families moving up, and owners who want to refinance. From the first call to the closing table, you will have one advisor who answers your questions and keeps the process moving on time.</p>
      <p>Please review the enclosed summary of options. If anything is unclear, call or write to us and we will gladly walk you through the details.</p>
      <p>Thank you for considering us for your home loan. Our team reviews every application with care, compares rates from many lenders, and explains each step in plain words. We help first-time buyers, families moving up, and owners who want to refinance. From the first call to the closing table, you will have one advisor who answers your questions and keeps the process moving on time.</p>
      <p>Please review the enclosed summary of options. If anything is unclear, call or write to us and we will gladly walk you through the details.</p>
    </div>
  </div>
  <div class="closing">
    <p class="sign-off">Sincerely,</p>
    <p class="signature">Derek Walsh</p>
    <p class="nmls">NMLS 61947 |<br>NMLS 472815</p>
  </div>
  <ul class="contact-list letter-footer">
    <li><svg><use href="#icon-phone"/></svg>614-208-3917</li>
    <li><svg><use href="#icon-pin"/></svg>48 Birchfield Court, Suite 314,<br>Marlow, OH 43952</li>
    <li><svg><use href="#icon-mail"/></svg>email@homebridle-example.com</li>
    <li><svg><use href="#icon-web"/></svg><span class="web">www.<span>homebridle</span>.com</span></li>
  </ul>
  <svg class="band" style="bottom:0;height:18px" viewBox="0 0 295 18" preserveAspectRatio="none"><rect y="6" width="295" height="12" fill="var(--blue)"/><path d="M0 0h30l18 18H0z" fill="var(--navy)"/><path d="M0 6h14l12 12H0z" fill="var(--blue)"/></svg>
</section>

<!-- square envelope -->
<section class="sheet envelope" aria-label="Envelope">
  <svg class="band" style="top:0;height:58px" viewBox="0 0 330 58" preserveAspectRatio="none"><path d="M0 0h330l-8 20c-3 6-6 8-12 9L170 56c-6 1-8 1-14 0L14 30C9 29 7 26 5 20z" fill="var(--blue)"/></svg>
  <div class="brand"><span class="brand-mark"></span>HomeBridle</div>
</section>

<!-- presentation folder -->
<section class="sheet folder" aria-label="Presentation folder">
  <svg class="band" style="top:0;left:0;width:20px;height:439px" viewBox="0 0 20 439" preserveAspectRatio="none"><rect width="13" height="439" fill="var(--blue)"/><path d="M6 0h13v36L0 52V18z" fill="var(--navy)"/></svg>
  <div class="brand"><span class="brand-mark"></span>HomeBridle</div>
</section>

<!-- DL envelope -->
<section class="sheet dl-envelope" aria-label="DL envelope">
  <div class="brand"><span class="brand-mark"></span>HomeBridle</div>
  <div class="person">
    <p class="person-name">Derek <b>Walsh</b></p>
    <p class="person-title">Business &amp; Personal Coach</p>
  </div>
  <ul class="contact-list">
    <li><svg><use href="#icon-phone"/></svg>614-208-3917</li>
    <li><svg><use href="#icon-pin"/></svg>48 Birchfield Court, Suite 314,<br>Marlow, OH 43952</li>
    <li><svg><use href="#icon-mail"/></svg>email@homebridle-example.com</li>
    <li><svg><use href="#icon-web"/></svg><span class="web">www.<span>homebridle</span>.com</span></li>
  </ul>
  <svg class="band" style="bottom:0;height:21px" viewBox="0 0 330 21" preserveAspectRatio="none"><rect y="7" width="330" height="14" fill="var(--blue)"/><path d="M0 0h32l16 21H0z" fill="var(--navy)"/><path d="M0 7h16l10 14H0z" fill="var(--blue)"/></svg>
  <p class="nmls">NMLS 61947 | NMLS 472815</p>
</section>
</body>
</html>
```